We need a DL size flyer, double sided, for our lawn mowing and gardening business, Kestrel Greens.

We want to run on the front side, the following promotion:
50% off lawn mowing, applies to first lawn mowed on any regular service,
applies to first 100 callers only, so call now!
Professional lawn mowing at an affordable price.

Logo at the bottom left, with Lawn and Garden Maintenance written just below logo.

On bottom Right contact details;
Tom and Gareth
Ph: 0487650912
Email: kestrelgreens@mailbox-example.com
www.kestrelgreens-example.com.au

Front side positioned horizontally, with a bright and colour full design in the background, with the offer of 50% Off lawn mowing in large letters along the top.

On the rear side, also positioned horizontally, a list of our services, stating;

At Kestrel Greens we specialise in the following services;
Lawn mowing
Edging
Blowing
Hedging
Pruning
Tree Loping
Weeding
Poisoning
Mulching
Fertilising
Rubbish removal
Planting
Lawn care and advice
Turf
And any other garden maintenance job,
No job too big or too small.
(No particular order, whatever fits best)
Also include our contact details,
Kestrel Greens
Ph 0487650912
www.kestrelgreens-example.com.au

Target Market(s)

Home owners, aged between 30-50 years old, moderate socio ecenomic status to more afluent areas.

Industry/Entity Type

Business

Requirements
Must have
• DL size, front and back, full colour.
Nice to have
• The writting stating "Kestrel Greens" in our logo is quite bland, if that could also be amended to make it more appealing, but change the writting design only not the actual logo.

```html
<!DOCTYPE html>
<html lang="en">
<head>
<meta charset="utf-8">
<title>Kestrel Greens – DL Flyer</title>
<link rel="stylesheet" href="https://fonts.googleapis.com/css2?family=Anton&family=Archivo+Black&family=Questrial&display=swap">
<style>
  :root {
    --stage: #8c6d52;
    --lawn: #8dc63f;
    --lawn-light: #c9e59a;
    --ink-dark: #14240a;
    --ink: #222222;
    --paper: #ffffff;
  }
  * { box-sizing: border-box; margin: 0; padding: 0; }
  html, body { width: 1200px; height: 761px; overflow: hidden; }
  body {
    background: var(--stage);
    font-family: "Questrial", "Century Gothic", sans-serif;
    position: relative;
  }
  .flyer {
    position: absolute;
    top: 40px;
    width: 322px;
    height: 680px;
    background: var(--lawn);
    overflow: hidden;
    box-shadow: 0 6px 18px rgba(0,0,0,.35);
  }
  .flyer--front { left: 250px; }
  .flyer--back { left: 628px; }

  .grass {
    position: absolute;
    left: 0; top: 0;
    width: 100%;
    background: linear-gradient(to bottom, var(--paper) 0%, var(--paper) 35%, var(--lawn-light) 70%, var(--lawn) 100%);
  }
  .flyer--front .grass { height: 135px; }
  .flyer--back .grass { height: 140px; }

  /* Front */
  .offer {
    position: absolute;
    left: 0; top: 14px;
    width: 100%;
    display: flex;
    justify-content: center;
    align-items: flex-start;
    color: var(--ink-dark);
  }
  .offer__number {
    font-family: "Anton", "Arial Narrow", sans-serif;
    font-size: 118px;
    line-height: 1;
    letter-spacing: -2px;
  }
  .offer__unit {
    display: flex;
    flex-direction: column;
    font-family: "Archivo Black", "Arial Black", sans-serif;
    margin-left: 4px;
    margin-top: 10px;
    line-height: .9;
  }
  .offer__percent { font-size: 44px; }
  .offer__off { font-size: 38px; }
  .offer__service {
    position: absolute;
    top: 142px; left: 0;
    width: 100%;
    text-align: center;
    font-family: "Archivo Black", "Arial Black", sans-serif;
    font-size: 34px;
    color: var(--ink-dark);
    letter-spacing: -.5px;
  }
  .terms {
    position: absolute;
    top: 204px; left: 0;
    width: 100%;
    height: 196px;
    background: var(--paper);
    color: var(--ink);
    text-align: center;
    padding: 28px 48px 0;
    font-size: 14.5px;
    line-height: 1.3;
  }
  .terms__cta {
    font-size: 21px;
    margin: 12px 0 12px;
  }
  .contact {
    position: absolute;
    top: 420px; left: 0;
    width: 100%;
    text-align: center;
    color: var(--ink-dark);
  }
  .contact__names { font-size: 21px; margin-bottom: 16px; }
  .contact__line { font-size: 16px; line-height: 1.3; }
  .brand {
    position: absolute;
    top: 568px; left: 0;
    width: 100%;
    display: flex;
    justify-content: center;
    align-items: center;
    gap: 10px;
    color: var(--ink-dark);
  }
  .brand__mark { width: 40px; height: 40px; border-radius: 50%; background: var(--paper); }
  .brand__name { font-size: 22px; }
  .brand__tagline {
    position: absolute;
    top: 636px; left: 0;
    width: 100%;
    text-align: center;
    font-size: 12px;
    color: var(--ink-dark);
  }

  /* Back */
  .services {
    position: absolute;
    top: 150px; left: 22px; right: 22px;
    color: var(--paper);
  }
  .services__intro { font-size: 16px; line-height: 1.2; margin-bottom: 18px; }
  .services__list {
    list-style: none;
    margin-left: 66px;
    font-size: 13.5px;
    line-height: 21px;
  }
  .services__tagline {
    margin-top: 22px;
    text-align: center;
    font-size: 15.5px;
  }
  .services__contact {
    margin-top: 26px;
    text-align: center;
    font-size: 15px;
    line-height: 1.3;
  }
</style>
</head>
<body>
  <section class="flyer flyer--front" aria-label="Flyer front">
    <div class="grass" role="img" aria-label="Illustrated grass blades along the top edge"></div>
    <div class="offer">
      <span class="offer__number">50</span>
      <span class="offer__unit"><span class="offer__percent">%</span><span class="offer__off">off</span></span>
    </div>
    <h1 class="offer__service">Lawn Mowing</h1>
    <div class="terms">
      <p>For the first lawn mowed on any regular service.<br>Applies to first 100 callers only.</p>
      <p class="terms__cta">Call now!</p>
      <p>Professional lawn mowing at an affordable price.</p>
    </div>
    <div class="contact">
      <p class="contact__names">Tom and Gareth</p>
      <p class="contact__line">0487650912</p>
      <p class="contact__line">kestrelgreens@mailbox-example.com</p>
      <p class="contact__line">www.kestrelgreens-example.com.au</p>
    </div>
    <div class="brand">
      <span class="brand__mark"></span>
      <span class="brand__name">Kestrel Greens</span>
    </div>
    <p class="brand__tagline">Lawn &amp; Gardening Maintenance</p>
  </section>

  <section class="flyer flyer--back" aria-label="Flyer back">
    <div class="grass" role="img" aria-label="Illustrated grass blades along the top edge"></div>
    <div class="services">
      <p class="services__intro">At Kestrel Greens we specialise<br>in the following services:</p>
      <ul class="services__list">
        <li>Lawn mowing</li>
        <li>Edging</li>
        <li>Blowing</li>
        <li>Hedging</li>
        <li>Pruning</li>
        <li>Tree Loping</li>
        <li>Weeding</li>
        <li>Poisoning</li>
        <li>Mulching</li>
        <li>Fertilising</li>
        <li>Rubbish removal</li>
        <li>Planting</li>
        <li>Lawn care and advice</li>
        <li>Turf</li>
        <li>And any other garden<br>maintenance job</li>
      </ul>
      <p class="services__tagline">No job too big or too small.</p>
      <div class="services__contact">
        <p>Kestrel Greens</p>
        <p>Ph 0487650912</p>
        <p>www.kestrelgreens-example.com.au</p>
      </div>
    </div>
  </section>
</body>
</html>
```